Shampoo and Shower Gel Packaging Design

I need a new packaging design for a men shampoo and shower gel bottle. The packaging must me black (black bottle/package) and the logo should be also monochrom.
For example, black matte bottle and black shiny logo on the packaging (not mandatory).
the design must contain maximum 3 colors.
1. black
2. white (text)
3. grey/dark blue/dark green (colors will be the difference between products parfumes/smell/scences.

Design must be minimalist/elegant/discrete.
Updates

Please check the photos i added for pure inspiration.

Target Market(s)

brand exclusively for MEN - premium clients

Industry/Entity Type

Cosmetics

Font styles to use
Sans Serif

Colors
1b1b1b
5c5c5c
aaaaaa
ffffff
3176b5

Requirements
Must have
• black background
• minimalist design

```html
<!DOCTYPE html>
<html lang="en">
<head>
<meta charset="utf-8">
<title>Norvan Cosmetics – Shampoo &amp; Shower Gel Label</title>
<link href="https://fonts.googleapis.com/css2?family=Josefin+Sans:wght@300;400&display=swap" rel="stylesheet">
<style>
  :root {
    --paper: #ffffff;
    --label-black: #000000;
    --ink-white: #ffffff;
  }
  html, body {
    margin: 0;
    padding: 0;
    width: 848px;
    height: 1200px;
    overflow: hidden;
    background: var(--paper);
  }
  .canvas {
    position: relative;
    width: 848px;
    height: 1200px;
    background: var(--paper);
  }
  .label {
    position: absolute;
    left: 74px;
    top: 106px;
    width: 698px;
    height: 984px;
    background: var(--label-black);
    border-radius: 5px;
  }
  .label__frame {
    position: absolute;
    left: 60px;
    top: 58px;
    width: 575px;
    height: 864px;
    border: 2px solid var(--ink-white);
    border-radius: 7px;
  }
  .brand {
    position: absolute;
    left: 0;
    right: 0;
    top: 505px;
    text-align: center;
    color: var(--ink-white);
    font-family: "Josefin Sans", sans-serif;
    font-weight: 300;
  }
  .brand__name {
    margin: 0;
    font-size: 56px;
    line-height: 1;
    letter-spacing: 0.62em;
    padding-left: 0.62em;
    font-weight: 300;
  }
  .brand__tagline {
    margin: 20px 0 0;
    font-size: 13px;
    letter-spacing: 0.72em;
    padding-left: 0.72em;
    font-weight: 300;
  }
  .product-name {
    position: absolute;
    left: 0;
    right: 0;
    top: 823px;
    margin: 0;
    text-align: center;
    color: var(--ink-white);
    font-family: "Josefin Sans", sans-serif;
    font-weight: 400;
    font-size: 21px;
    font-variant: small-caps;
    letter-spacing: 0.14em;
  }
</style>
</head>
<body>
  <main class="canvas">
    <section class="label">
      <div class="label__frame"></div>
      <div class="brand">
        <h1 class="brand__name">NORVAN</h1>
        <p class="brand__tagline">COSMETICS</p>
      </div>
      <p class="product-name">Shampoo &amp; Shower Gel</p>
    </section>
  </main>
</body>
</html>
```